Verimont Designs business card

Front of card should be logo and back of card should be communication info.
Please note: reverse the logo color. Card should be black and everything else white.

Industry/Entity Type

Custom home design/construction

Contact Information for Business Card

Verimont Designs, LLC 614-382-9017 verimontdesigns@quillmail.example

Requirements
Must have
• Square card, Logo on front, communication info on back and perhaps a mini version of the logo on back also. Black card/white lettering. Double sides square card.
Nice to have
• I want to keep it simple. Our product (custom homes) speak for themselves.

```html
<!DOCTYPE html>
<html lang="en">
<head>
<meta charset="utf-8">
<title>Verimont Designs — Business Card</title>
<link href="https://fonts.googleapis.com/css2?family=Montserrat:wght@400;500;700;800&family=Poppins:wght@400&display=swap" rel="stylesheet">
<style>
  :root {
    --backdrop: #e6e3df;
    --card: #231f20;
    --ink: #ffffff;
    --ink-muted: #9a9698;
    --rule: #6d696b;
  }
  html, body {
    margin: 0;
    width: 1200px;
    height: 800px;
    overflow: hidden;
    background: var(--backdrop);
  }
  .canvas {
    position: relative;
    width: 1200px;
    height: 800px;
  }
  .card {
    position: absolute;
    top: 160px;
    width: 480px;
    height: 480px;
    border-radius: 28px;
    background: var(--card);
    box-shadow: 0 12px 30px rgba(0,0,0,0.18);
    color: var(--ink);
    box-sizing: border-box;
  }
  .card--front { left: 90px; }
  .card--back { left: 630px; }

  /* Front */
  .card--front {
    display: flex;
    align-items: center;
    justify-content: center;
  }
  .brand-name {
    font-family: "Montserrat", sans-serif;
    font-weight: 700;
    font-size: 36px;
    letter-spacing: 2px;
    color: var(--ink);
    text-transform: uppercase;
  }

  /* Back */
  .card--back { padding: 56px 48px 0 52px; }
  .brand-name--mini {
    display: block;
    font-size: 17px;
    letter-spacing: 2px;
    text-align: center;
    margin-bottom: 34px;
  }
  .person-first {
    font-family: "Montserrat", sans-serif;
    font-weight: 800;
    font-size: 46px;
    line-height: 1;
    letter-spacing: 1px;
    text-transform: uppercase;
  }
  .person-last {
    font-family: "Montserrat", sans-serif;
    font-weight: 500;
    font-size: 46px;
    line-height: 1.05;
    letter-spacing: 1px;
    text-transform: uppercase;
  }
  .person-role {
    font-family: "Montserrat", sans-serif;
    font-weight: 400;
    font-size: 15px;
    letter-spacing: 2px;
    color: var(--ink-muted);
    text-transform: uppercase;
    margin-top: 8px;
  }
  .contact-block {
    display: flex;
    gap: 16px;
    margin-top: 26px;
  }
  .contact-rule {
    width: 1px;
    background: var(--rule);
    height: 150px;
  }
  .contact-list {
    list-style: none;
    margin: 0;
    padding: 0;
  }
  .contact-item {
    display: flex;
    align-items: center;
    gap: 10px;
    font-family: "Poppins", sans-serif;
    font-size: 15px;
    margin-bottom: 14px;
  }
  .contact-icon {
    width: 22px;
    height: 22px;
    flex: none;
  }
  .card-rule {
    position: absolute;
    left: 52px;
    right: 48px;
    bottom: 56px;
    height: 1px;
    background: var(--rule);
  }
</style>
</head>
<body>
<div class="canvas">
  <section class="card card--front" aria-label="Card front">
    <span class="brand-name">Verimont Designs</span>
  </section>

  <section class="card card--back" aria-label="Card back">
    <span class="brand-name brand-name--mini">Verimont Designs</span>
    <div class="person-first">Everett</div>
    <div class="person-last">Marlowe</div>
    <div class="person-role">Managing Director</div>
    <div class="contact-block">
      <div class="contact-rule"></div>
      <ul class="contact-list">
        <li class="contact-item">
          <svg class="contact-icon" viewBox="0 0 22 22" aria-hidden="true">
            <circle cx="11" cy="11" r="10" fill="none" stroke="#9a9698" stroke-width="1.2"/>
            <path d="M8 6.5c.6-.3 1 .1 1.3.7l.6 1.3c.2.5 0 .8-.4 1.1l-.4.3c.5 1.2 1.5 2.2 2.7 2.7l.3-.4c.3-.4.6-.6 1.1-.4l1.3.6c.6.3 1 .7.7 1.3-.5 1-1.4 1.6-2.5 1.3-2.6-.8-4.6-2.8-5.4-5.4-.3-1.1.3-2 1.3-2.5z" fill="#ffffff"/>
          </svg>
          614-382-9017
        </li>
        <li class="contact-item">
          <svg class="contact-icon" viewBox="0 0 22 22" aria-hidden="true">
            <circle cx="11" cy="11" r="10" fill="none" stroke="#9a9698" stroke-width="1.2"/>
            <rect x="6" y="7.5" width="10" height="7" rx="1" fill="none" stroke="#ffffff" stroke-width="1.2"/>
            <path d="M6.3 8l4.7 3.5L15.7 8" fill="none" stroke="#ffffff" stroke-width="1.2"/>
          </svg>
          verimontdesigns@quillmail.example
        </li>
      </ul>
    </div>
    <div class="card-rule"></div>
  </section>
</div>
</body>
</html>
```